Service Offering Graphic Design

We need a small graphic designed which can be placed on our website, flyers etc. to outline our service offering - Hopefully this is a very simple task.

It needs to be professional and business oriented.

I have attached two pictures:
Picture1 shows our two high level services and the composition of each below it. Underpinning both is the following statements:
"Contextual"
"Vendor Agnostic"
You can place these words to represent that approach as you feel fits.

Picture titled 'quad' - an example from another company (not as something we would like you to copy). Its to show someone and say ' high level, this is what we do'.

No background please - It exists to be embedded as a png most likely.

Font on our website is Sans Serif - Could we continue this is in the graphic.

Target Market(s)

Other business

Industry/Entity Type

Defence

Font styles to use
Sans Serif

Colors

Designer to choose colors to be used in the design.

Requirements
Must have
• The text
Should not have
• Little logos of men or light bulbs
• Logo is added for detail on colour only.

```html
<!DOCTYPE html>
<html lang="en">
<head>
<meta charset="utf-8">
<title>Service Offering</title>
<link rel="stylesheet" href="https://fonts.googleapis.com/css2?family=Roboto+Condensed:wght@400&display=swap">
<style>
  :root {
    --ink: #2b2a29;
    --red: #e11f26;
    --white: #ffffff;
    --market: #c45cae;
    --idea: #5076c4;
    --prototype: #00b4f0;
    --concept: #8ce3cf;
    --systems: #ff737f;
    --requirements: #ff8a6d;
    --test: #ffc662;
    --training: #ffcc94;
  }
  html, body {
    margin: 0;
    padding: 0;
    width: 1200px;
    height: 1200px;
    overflow: hidden;
    background: var(--white);
  }
  .service-wheel {
    display: block;
    width: 1200px;
    height: 1200px;
  }
  .band-dark { fill: var(--ink); }
  .band-red { fill: var(--red); }
  .blade { stroke: var(--white); stroke-width: 2; }
  .blade--market { fill: var(--market); }
  .blade--idea { fill: var(--idea); }
  .blade--prototype { fill: var(--prototype); }
  .blade--concept { fill: var(--concept); }
  .blade--systems { fill: var(--systems); }
  .blade--requirements { fill: var(--requirements); }
  .blade--test { fill: var(--test); }
  .blade--training { fill: var(--training); }
  .hub-capability { fill: var(--red); }
  .hub-research { fill: var(--ink); }
  .blade-label {
    font-family: "Roboto Condensed", "Arial Narrow", sans-serif;
    font-size: 42px;
    fill: var(--ink);
    dominant-baseline: central;
  }
  .hub-label {
    font-family: "Roboto Condensed", "Arial Narrow", sans-serif;
    font-size: 46px;
    fill: var(--white);
    text-anchor: middle;
  }
</style>
</head>
<body>
<svg class="service-wheel" viewBox="0 0 1500 1500" xmlns="http://www.w3.org/2000/svg" role="img" aria-label="Service offering wheel: Research and Development and Capability Development">
  <defs>
    <path id="blade-shape" d="M108,888 L120,572 C140,800 300,990 560,1008 C700,1015 820,960 880,890 C820,1000 700,1100 540,1105 C330,1110 180,1000 108,888 Z"/>
    <path id="band-shape" d="M108,888 L120,572 L206,585 C260,760 400,880 743,941 L880,890 C820,1000 700,1100 540,1105 C330,1110 180,1000 108,888 Z"/>
    <path id="midline-out" d="M114,730 C170,930 370,1055 580,1055 C700,1055 800,1000 880,890"/>
    <path id="midline-in" d="M880,890 C800,1000 700,1055 580,1055 C370,1055 170,930 114,730"/>
  </defs>

  <g class="bands">
    <use href="#band-shape" class="band-dark" transform="rotate(0 750 750)"/>
    <use href="#band-shape" class="band-dark" transform="rotate(45 750 750)"/>
    <use href="#band-shape" class="band-dark" transform="rotate(90 750 750)"/>
    <use href="#band-shape" class="band-red" transform="rotate(135 750 750)"/>
    <use href="#band-shape" class="band-red" transform="rotate(180 750 750)"/>
    <use href="#band-shape" class="band-red" transform="rotate(225 750 750)"/>
    <use href="#band-shape" class="band-red" transform="rotate(270 750 750)"/>
    <use href="#band-shape" class="band-dark" transform="rotate(315 750 750)"/>
  </g>

  <g class="blades">
    <use href="#blade-shape" class="blade blade--prototype" transform="rotate(0 750 750)"/>
    <use href="#blade-shape" class="blade blade--idea" transform="rotate(45 750 750)"/>
    <use href="#blade-shape" class="blade blade--market" transform="rotate(90 750 750)"/>
    <use href="#blade-shape" class="blade blade--systems" transform="rotate(135 750 750)"/>
    <use href="#blade-shape" class="blade blade--requirements" transform="rotate(180 750 750)"/>
    <use href="#blade-shape" class="blade blade--test" transform="rotate(225 750 750)"/>
    <use href="#blade-shape" class="blade blade--training" transform="rotate(270 750 750)"/>
    <use href="#blade-shape" class="blade blade--concept" transform="rotate(315 750 750)"/>
  </g>

  <g class="hub">
    <path class="hub-capability" d="M559,750 L559,740 L622,608 L760,559 L892,622 L941,750 Z"/>
    <path class="hub-research" d="M559,750 L941,750 L941,760 L878,892 L743,941 L608,878 Z"/>
    <text class="hub-label" x="748" y="658">Capability</text>
    <text class="hub-label" x="748" y="716">Development</text>
    <text class="hub-label" x="748" y="814">Research and</text>
    <text class="hub-label" x="748" y="872">Development</text>
  </g>

  <g class="labels">
    <text class="blade-label" transform="rotate(0 750 750)"><textPath href="#midline-out" startOffset="40%" text-anchor="middle">Prototyping</textPath></text>
    <text class="blade-label" transform="rotate(45 750 750)"><textPath href="#midline-out" startOffset="42%" text-anchor="middle">Idea Generation &amp; Screening</textPath></text>
    <text class="blade-label" transform="rotate(90 750 750)"><textPath href="#midline-in" startOffset="60%" text-anchor="middle">Market Investigation</textPath></text>
    <text class="blade-label" transform="rotate(135 750 750)"><textPath href="#midline-in" startOffset="60%" text-anchor="middle">Systems Design &amp; Integration</textPath></text>
    <text class="blade-label" transform="rotate(180 750 750)"><textPath href="#midline-in" startOffset="60%" text-anchor="middle">Requirements Engineering</textPath></text>
    <text class="blade-label" transform="rotate(225 750 750)"><textPath href="#midline-in" startOffset="58%" text-anchor="middle">Test &amp; Evaluation</textPath></text>
    <text class="blade-label" transform="rotate(270 750 750)"><textPath href="#midline-in" startOffset="58%" text-anchor="middle">Training &amp; Support</textPath></text>
    <text class="blade-label" transform="rotate(315 750 750)"><textPath href="#midline-out" startOffset="42%" text-anchor="middle">Concept Development</textPath></text>
  </g>
</svg>
</body>
</html>
```